Marlowe Holdings LLC - Business Cards

Need the following information on the cards:

Name: Dean R Vossler
Title: Chief Executive Manager

Business address:
412 N Ridgeview Lane #118
Maple Crest, Il 60412

Phone: (630) 555-0148 - Business
KPV FFL license number: 5-21-xxx-xx-xx-04519
Email: dean.vossler@marloweholdingsffl.com

Target Market(s)

Firearm owners

Industry/Entity Type

Firearms industry,

Contact Information for Business Card

Contact number, name and title, web page address, email, business address and kpv license number,

Requirements
Must have
• Name, title, business address, phone numbers, KPV license numbers, web page address and email address.
Nice to have
• Cellphone number,

```html
<!DOCTYPE html>
<html lang="en">
<head>
<meta charset="utf-8">
<title>Marlowe Holdings LLC – Business Cards</title>
<link rel="stylesheet" href="https://fonts.googleapis.com/css2?family=Roboto+Slab:wght@300;400;700&display=swap">
<style>
  :root {
    --page: #ffffff;
    --ink: #231f20;
    --card-dark: #231f20;
    --accent: #d2232a;
    --paper: #ffffff;
  }
  * { box-sizing: border-box; margin: 0; padding: 0; }
  html, body { width: 1200px; height: 1200px; overflow: hidden; background: var(--page); }
  body { position: relative; font-family: "Roboto Slab", Georgia, serif; color: var(--ink); }

  .card { position: absolute; left: 198px; width: 811px; height: 464px; }
  .card-front { top: 121px; background: var(--card-dark); }
  .card-back { top: 622px; background: var(--paper); border: 1.5px solid var(--ink); }

  .front-emblem {
    position: absolute; left: 230px; top: 82px; width: 351px; height: 280px;
    display: flex; flex-direction: column; align-items: center; justify-content: center; gap: 16px;
  }
  .emblem-art { width: 220px; height: 170px; border-radius: 50%; background: radial-gradient(circle, #3a3435 0%, #2b2627 70%); }
  .brand-row { display: flex; align-items: center; gap: 12px; }
  .brand-dot { width: 14px; height: 14px; border-radius: 50%; background: var(--accent); }
  .brand-name { color: #ffffff; font-weight: 700; font-size: 30px; letter-spacing: 1px; white-space: nowrap; }

  .holder-name { position: absolute; left: 36px; top: 44px; font-weight: 700; font-size: 45px; line-height: 1.2; letter-spacing: -0.3px; white-space: nowrap; }
  .holder-title { position: absolute; left: 38px; top: 100px; font-weight: 300; font-size: 22px; line-height: 1.2; white-space: nowrap; }

  .back-brand {
    position: absolute; left: 648px; top: 48px; width: 130px; text-align: center;
    color: var(--accent); font-weight: 700; font-size: 15px; line-height: 1.25;
  }
  .back-brand-art { width: 92px; height: 56px; margin: 0 auto 8px; border-radius: 50% 50% 8px 8px; background: #f1dede; }

  .divider { position: absolute; left: 35px; top: 188px; width: 145px; height: 2px; background: var(--ink); }

  .contact { position: absolute; left: 36px; display: flex; align-items: flex-start; }
  .contact .icon { width: 18px; height: 18px; flex: none; margin-top: 5px; }
  .contact .value { margin-left: 17px; font-weight: 300; font-size: 25px; line-height: 26px; white-space: nowrap; }
  .c-phone { top: 206px; }
  .c-license { top: 233px; }
  .c-email { top: 279px; }
  .c-web { top: 306px; }
  .c-address { top: 352px; }
</style>
</head>
<body>

<section class="card card-front">
  <div class="front-emblem">
    <div class="emblem-art" role="img" aria-label="Emblem illustration area: standing dog over red sunburst ring with crossed rifles"></div>
    <div class="brand-row">
      <span class="brand-dot"></span>
      <span class="brand-name">Marlowe Holdings LLC</span>
    </div>
  </div>
</section>

<section class="card card-back">
  <h1 class="holder-name">Dean R Vossler</h1>
  <p class="holder-title">Chief Executive Manager</p>

  <div class="back-brand">
    <div class="back-brand-art" role="img" aria-label="Small emblem illustration area: dog and crossed rifles"></div>
    Marlowe Holdings LLC
  </div>

  <div class="divider"></div>

  <div class="contact c-phone">
    <svg class="icon" viewBox="0 0 18 18"><rect width="18" height="18" rx="3" fill="#231f20"/><path d="M5.2 4.2l2 .1.8 2.4-1.2.9c.6 1.4 1.6 2.4 3 3l.9-1.2 2.4.8.1 2c0 .5-.5 1-1 1C8 13.1 4.9 10 4.2 5.2c0-.5.5-1 1-1z" fill="#fff"/></svg>
    <span class="value">+1 630 555 0148</span>
  </div>
  <div class="contact c-license">
    <svg class="icon" viewBox="0 0 18 18"><rect width="18" height="18" rx="3" fill="#231f20"/><rect x="3.5" y="5" width="11" height="8" rx="1" fill="none" stroke="#fff" stroke-width="1"/><circle cx="6.5" cy="8" r="1" fill="#fff"/><path d="M5 11h3M9.5 7.5h3.5M9.5 9.5h3.5" stroke="#fff" stroke-width="1"/></svg>
    <span class="value">5-21-xxx-xx-xx-04519</span>
  </div>
  <div class="contact c-email">
    <svg class="icon" viewBox="0 0 18 18"><rect width="18" height="18" rx="3" fill="#231f20"/><rect x="4" y="5.5" width="10" height="7" fill="none" stroke="#fff" stroke-width="1"/><path d="M4 5.5l5 4 5-4" fill="none" stroke="#fff" stroke-width="1"/></svg>
    <span class="value">dean.vossler@marloweholdingsffl.com</span>
  </div>
  <div class="contact c-web">
    <svg class="icon" viewBox="0 0 18 18"><rect width="18" height="18" rx="3" fill="#231f20"/><circle cx="9" cy="9" r="5" fill="none" stroke="#fff" stroke-width="1"/><ellipse cx="9" cy="9" rx="2.2" ry="5" fill="none" stroke="#fff" stroke-width="1"/><path d="M4 9h10" stroke="#fff" stroke-width="1"/></svg>
    <span class="value">marloweholdingsffl.com</span>
  </div>
  <div class="contact c-address">
    <svg class="icon" viewBox="0 0 18 18"><rect width="18" height="18" rx="3" fill="#231f20"/><path d="M9 14s-4-4.2-4-7a4 4 0 0 1 8 0c0 2.8-4 7-4 7z" fill="#fff"/><circle cx="9" cy="7" r="1.4" fill="#231f20"/></svg>
    <span class="value">412 N Ridgeview Lane<br>#118 Maple Crest,<br>Il 60412</span>
  </div>
</section>

</body>
</html>
```